Business card design for Verdanta Building Systems
Verdanta Building Systems
Professional
Trevor Halloway
Director
418/37 Brindle St
Port Melbourne
VIC 3207
trevor@verdantabuilding.example.au
www.verdantabuilding.example.au
- Architectural Sunscreens
- Privacy Screens
- Modular/Continuous louvres
- Acoustic louvres
- Opening roof systems
- Handrail systems
- Custom Aluminium facades
- Architectural timber structures
this is the colours we like
front of card and back of card

```html
<!DOCTYPE html>
<html lang="en">
<head>
<meta charset="utf-8">
<title>Verdanta Building Systems – Business Card</title>
<link rel="stylesheet" href="https://fonts.googleapis.com/css2?family=Montserrat:wght@400;500;600;700&display=swap">
<style>
  :root {
    --green: #1f8a4c;
    --green-dark: #146a38;
    --green-light: #2fa05c;
    --ink: #4a4f4c;
    --muted: #8a8f8c;
    --paper: #ffffff;
    --stage: #ecebe6;
  }
  * { margin: 0; padding: 0; box-sizing: border-box; }
  html, body {
    width: 1200px; height: 629px; overflow: hidden;
    background: var(--stage);
    font-family: "Montserrat", Arial, sans-serif;
  }
  .stage {
    width: 1200px; height: 629px;
    display: flex; align-items: center; justify-content: center; gap: 60px;
  }
  .card {
    position: relative;
    width: 520px; height: 297px;
    box-shadow: 0 10px 28px rgba(0,0,0,0.18);
    overflow: hidden;
  }
  /* Front */
  .card-front { background: var(--paper); }
  .brand {
    position: absolute; left: 110px; top: 62px;
    display: flex; align-items: center; gap: 12px;
  }
  .brand-dot {
    width: 34px; height: 34px; border-radius: 50%;
    background: var(--green);
  }
  .brand-name {
    font-size: 30px; font-weight: 600; letter-spacing: 1px;
    color: var(--green); line-height: 1;
  }
  .brand-tagline {
    position: absolute; left: 156px; top: 100px;
    font-size: 7px; letter-spacing: 2.6px; color: var(--muted);
    text-transform: uppercase;
  }
  .person {
    position: absolute; left: 228px; top: 138px;
  }
  .person-name { font-size: 12px; font-weight: 700; color: var(--green); }
  .person-role { font-size: 9px; color: var(--muted); margin-top: 2px; }
  .contact {
    position: absolute; left: 330px; top: 132px;
    padding-left: 10px; border-left: 2px solid var(--green);
    font-size: 8px; line-height: 1.7; color: var(--ink);
  }
  .contact-row { display: flex; align-items: center; gap: 5px; }
  .contact-row svg { width: 8px; height: 8px; fill: var(--green); }
  .address {
    position: absolute; left: 26px; bottom: 46px;
    font-size: 7px; letter-spacing: 0.4px; color: var(--muted);
  }
  .web-band {
    position: absolute; left: 0; right: 0; bottom: 0; height: 30px;
    background: linear-gradient(90deg, var(--green-dark), var(--green-light));
    display: flex; align-items: center; justify-content: center;
    color: #fff; font-size: 8px; letter-spacing: 3px;
  }
  .web-line {
    position: absolute; left: 0; right: 0; bottom: 30px; height: 3px;
    background: #d9ece0;
  }
  /* Back */
  .card-back {
    background: linear-gradient(135deg, var(--green-light) 0%, var(--green) 45%, var(--green-dark) 100%);
  }
  .back-mark {
    position: absolute; left: 250px; top: 40px;
    width: 150px; height: 150px; border-radius: 50%;
    background: radial-gradient(circle at 40% 35%, rgba(255,255,255,0.22), rgba(255,255,255,0.06) 70%);
  }
  .back-web {
    position: absolute; left: 26px; bottom: 24px;
    font-size: 7px; letter-spacing: 1.5px; color: rgba(255,255,255,0.75);
  }
</style>
</head>
<body>
<main class="stage">
  <section class="card card-front" aria-label="Card front">
    <div class="brand">
      <span class="brand-dot"></span>
      <span class="brand-name">VERDANTA</span>
    </div>
    <div class="brand-tagline">Building Systems</div>

    <div class="person">
      <div class="person-name">Trevor Halloway</div>
      <div class="person-role">Director</div>
    </div>

    <div class="contact">
      <div class="contact-row">
        <svg viewBox="0 0 10 10"><path d="M2 0h2l1 3-1.5 1a6 6 0 0 0 2.5 2.5L7 5l3 1v2a2 2 0 0 1-2 2A8 8 0 0 1 0 2a2 2 0 0 1 2-2z"/></svg>
        T +61 3 9000 4417
      </div>
      <div class="contact-row">
        <svg viewBox="0 0 10 10"><rect x="2" y="0" width="6" height="10" rx="1"/></svg>
        M 0400 118 225
      </div>
      <div class="contact-row">
        <svg viewBox="0 0 10 10"><path d="M0 2h10v6H0z M0 2l5 3.5L10 2" /></svg>
        trevor@verdantabuilding.example.au
      </div>
    </div>

    <div class="address">418/37 Brindle St, Port Melbourne VIC 3207</div>

    <div class="web-line"></div>
    <div class="web-band">www.verdantabuilding.example.au</div>
  </section>

  <section class="card card-back" aria-label="Card back">
    <div class="back-mark"></div>
    <div class="back-web">www.verdantabuilding.example.au</div>
  </section>
</main>
</body>
</html>
```